Intermodal Trucking Company Website

My client is a trucking company that takes the containers you see on the back of a ship or railroad car and delivers them in the midwestern part of the United States. Here are some of their competitors Websites and their logo to use as part of the design.

http://www.varnekhaulers.example/
https://www.plirext.example/
http://www.brontagefreight.example/
https://www.lqp-xy.example/

Industry/Entity Type

Trucking Company

Number of Pages Required

2 page

Requirements
Must have
• Website must be professional and the design needs to be suitable for a responsive Website.
Should not have
• Please do not submit designs with misspellings. Designs with misspellings will be eliminated.

```html
<!DOCTYPE html>
<html lang="en">
<head>
<meta charset="utf-8">
<title>Tandem Rail Haul INC – Intermodal Container Transport</title>
<link href="https://fonts.googleapis.com/css2?family=Roboto:ital,wght@0,300;0,400;0,500;0,700;1,300;1,400&display=swap" rel="stylesheet">
<style>
:root{
  --red:#e8362f;
  --red-light:#f26a63;
  --ink:#222;
  --text:#444;
  --muted:#888;
  --bg-grey:#efefef;
  --line:#ddd;
  --white:#fff;
  --hero-top:#b9c3cc;
  --hero-bottom:#4a4744;
}
*{margin:0;padding:0;box-sizing:border-box}
html,body{width:1200px;height:2171px;overflow:hidden}
body{font-family:"Roboto",Arial,sans-serif;color:var(--text);background:var(--white);position:relative}
.top-strip{height:4px;background:var(--red)}
.site-header{height:68px;display:flex;align-items:center;padding:0 46px 0 50px;position:relative}
.brand{display:flex;align-items:center;gap:8px;font-weight:700;font-size:17px;color:var(--red)}
.brand-dot{width:14px;height:14px;border-radius:50%;background:var(--red)}
.main-nav{position:absolute;left:457px;top:26px;display:flex;gap:0}
.main-nav a{font-size:14px;color:var(--ink);text-decoration:none;font-weight:500}
.main-nav a:nth-child(1){margin-right:38px}
.main-nav a:nth-child(2){margin-right:37px}
.header-actions{margin-left:auto;display:flex;align-items:center;gap:24px}
.chat-link{font-size:13px;color:var(--ink);display:flex;align-items:center;gap:4px}
.quote-btn{background:var(--red);color:var(--white);font-size:13px;font-weight:500;padding:9px 12px;border-radius:5px}
.hero{height:493px;position:relative;background:linear-gradient(180deg,var(--hero-top) 0%,#9aa4ad 45%,#6f6a63 70%,var(--hero-bottom) 100%)}
.hero-badge{position:absolute;left:492px;top:195px;width:218px;height:218px;border-radius:50%;background:rgba(90,90,90,.75);color:var(--white);display:flex;flex-direction:column;align-items:center;justify-content:center;text-align:center;line-height:1.1}
.hero-badge .thin{font-weight:300;font-size:21px;letter-spacing:2px}
.hero-badge .bold{font-weight:700;font-size:30px;letter-spacing:1px}
.info-bar{height:34px;background:#f4f4f4;border-top:1px solid var(--line);border-bottom:1px solid var(--line);display:flex;align-items:center;padding:0 52px;font-size:13px;color:var(--muted);gap:30px}
.info-bar span{display:flex;align-items:center;gap:7px}
.info-social{margin-left:auto;display:flex;gap:26px;align-items:center}
.sq{width:15px;height:15px;border-radius:2px}
.section-title{text-align:center;font-size:21px;font-weight:500;color:var(--ink)}
.section-title em{font-style:normal;color:var(--red)}
.dots{border-top:1px dashed var(--red);margin:0 51px}
.welcome{height:113px;padding-top:8px}
.welcome .dots{margin-top:8px}
.welcome p{text-align:center;font-size:12.5px;line-height:20px;color:var(--ink);width:1050px;margin:21px auto 0}
.services{height:308px;background:var(--bg-grey);padding-top:21px}
.services .dots{margin-top:10px}
.service-grid{display:flex;gap:28px;padding:0 51px;margin-top:46px}
.service-card{width:253px;height:168px;border-radius:0 0 18px 18px;overflow:hidden;display:flex;flex-direction:column}
.service-photo{flex:1}
.service-label{height:43px;background:linear-gradient(90deg,var(--red),var(--red-light));color:var(--white);font-weight:500;font-size:15px;display:flex;align-items:center;justify-content:center;border-radius:0 18px 18px 18px}
.process{height:275px;padding-top:21px;position:relative}
.process .dots{margin-top:10px}
.process-steps{position:relative;height:180px}
.process-line{position:absolute;top:103px;height:1px;background:var(--red);width:66px}
.step{position:absolute;top:56px;width:140px;margin-left:-70px;text-align:center}
.step-icon{width:94px;height:94px;border-radius:50%;background:var(--red);margin:0 auto;display:flex;align-items:center;justify-content:center}
.step-icon.active{box-shadow:inset 0 0 0 4px var(--red),inset 0 0 0 6px var(--white)}
.step-label{margin-top:24px;font-size:13.5px;font-weight:500;color:var(--ink)}
.step-label.active{color:var(--red)}
.testimonials{height:358px;background:var(--bg-grey);padding-top:19px;position:relative}
.testimonials .dots{margin-top:10px}
.quote{position:absolute;width:520px;display:flex;gap:26px;align-items:flex-start}
.quote p{font-style:italic;font-weight:300;font-size:12.5px;line-height:20px;color:var(--text)}
.quote cite{display:block;font-style:normal;font-size:12.5px;color:var(--ink);margin-top:8px}
.quote.left{text-align:right}
.avatar{width:76px;height:76px;border-radius:50%;flex:none;background:radial-gradient(circle at 50% 40%,#d9c3b3,#8b7a6e)}
.divider-v{position:absolute;left:600px;top:100px;height:216px;border-left:1px dashed var(--red)}
.divider-h{position:absolute;left:51px;right:51px;top:211px;border-top:1px dashed var(--red)}
.mail-strip{height:94px;display:flex;align-items:center;padding:0 51px}
.mail-strip .lbl{font-size:13px;font-weight:500;color:var(--ink);margin:0 29px 0 21px}
.field{width:254px;height:33px;border:1px solid var(--line);background:#f6f6f6;border-radius:4px;font-size:12.5px;color:#aaa;padding:0 14px;display:flex;align-items:center;margin-right:18px}
.submit{margin-left:2px;background:var(--red);color:var(--white);font-weight:500;font-size:13px;width:90px;height:33px;border-radius:4px;display:flex;align-items:center;justify-content:center}
.site-footer{height:424px;background:var(--bg-grey);position:relative;padding-top:24px}
.footer-col{position:absolute;top:24px}
.footer-col h3{font-size:18px;font-weight:500;color:var(--ink);margin-bottom:18px}
.footer-col p{font-size:12.5px;line-height:19.5px;color:var(--ink);margin-bottom:14px}
.contact-col{left:52px;width:255px}
.contact-col strong{font-weight:500}
.hq-col{left:333px;width:535px}
.hq-col h3{text-align:center}
.map{height:225px;background:linear-gradient(135deg,#eceae4 0%,#e3e0d8 40%,#a9c9ea 55%,#9cc1e6 100%)}
.about-col{left:896px;width:252px}
.foot-social{display:flex;gap:16px;margin-top:4px}
.foot-social span{width:11px;height:11px;border-radius:50%;background:var(--ink)}
.footer-rule{position:absolute;left:51px;right:51px;top:345px;border-top:1px solid #888}
.footer-bottom{position:absolute;left:51px;right:51px;top:370px;display:flex;align-items:center;justify-content:space-between;font-size:12px;color:var(--ink)}
.footer-brand{display:flex;align-items:center;gap:7px;font-weight:700;font-size:15px;color:var(--red)}
.bottom-strip{position:absolute;left:0;right:0;bottom:0;height:7px;background:var(--red)}
</style>
</head>
<body>
<div class="top-strip"></div>
<header class="site-header">
  <div class="brand"><span class="brand-dot"></span>Tandem Rail Haul INC</div>
  <nav class="main-nav"><a href="#">Our Company</a><a href="#">Services</a><a href="#">Contact Us</a></nav>
  <div class="header-actions">
    <span class="chat-link">Chat
      <svg width="14" height="12" viewBox="0 0 14 12"><path d="M2 1h10a1 1 0 0 1 1 1v5a1 1 0 0 1-1 1H6l-3 3V8H2a1 1 0 0 1-1-1V2a1 1 0 0 1 1-1z" fill="none" stroke="#222" stroke-width="1.3"/></svg></span>
    <span class="quote-btn">Request a Quote</span>
  </div>
</header>

<section class="hero" role="img" aria-label="Container truck driving along a coastal highway in bright sunlight">
  <div class="hero-badge"><span class="thin">TRANSPORT</span><span class="bold">SOLUTIONS</span><span class="thin">FOR</span><span class="thin">CONTAINERS</span></div>
</section>

<div class="info-bar">
  <span><svg width="12" height="12" viewBox="0 0 12 12"><path d="M3 1l2 2-1 2c1 2 2 3 3 3l2-1 2 2-2 2C4 11 1 8 1 3z" fill="#999"/></svg>+1 800 555 01 42</span>
  <span><svg width="13" height="10" viewBox="0 0 13 10"><rect x="0.5" y="0.5" width="12" height="9" fill="#999"/><path d="M1 1l5.5 4L12 1" stroke="#f4f4f4" fill="none"/></svg>dispatch@tandemrailhaul.example</span>
  <div class="info-social">
    <span class="sq" style="background:#3b5998"></span>
    <span class="sq" style="background:#2aa3db"></span>
    <span class="sq" style="background:#e0452e"></span>
    <svg width="13" height="13" viewBox="0 0 13 13"><circle cx="5.5" cy="5.5" r="4" fill="none" stroke="#999" stroke-width="1.6"/><path d="M8.5 8.5L12 12" stroke="#999" stroke-width="1.8"/></svg>
  </div>
</div>

<section class="welcome">
  <h2 class="section-title">Welcome to <em>Tandem Rail Haul INC</em></h2>
  <div class="dots"></div>
  <p>Call us for all your intermodal container movement needs out of the Kansas City, KS or MO area. We have been in business for over 20 years handling all types of container movement including hazmat movements to anywhere within the 48 states.</p>
</section>

<section class="services">
  <h2 class="section-title">Our <em>Services</em></h2>
  <div class="dots"></div>
  <div class="service-grid">
    <div class="service-card"><div class="service-photo" role="img" aria-label="Heavy haul truck carrying oversized machinery" style="background:linear-gradient(180deg,#a9c3d9,#6c6458)"></div><div class="service-label">Heavy Haul</div></div>
    <div class="service-card"><div class="service-photo" role="img" aria-label="Flatbed truck loaded with a yellow container by a forest" style="background:linear-gradient(180deg,#5d7457,#8b8a80)"></div><div class="service-label">Mixed Load &amp; Truckload</div></div>
    <div class="service-card"><div class="service-photo" role="img" aria-label="Tanker trucks parked under a sunset sky" style="background:linear-gradient(180deg,#b8837b,#6b6b70)"></div><div class="service-label">Logistics</div></div>
    <div class="service-card"><div class="service-photo" role="img" aria-label="Dedicated semi truck with a branded trailer" style="background:linear-gradient(180deg,#8bb0d6,#2c3446)"></div><div class="service-label">Dedicated</div></div>
  </div>
</section>

<section class="process">
  <h2 class="section-title">Process <em>Cargo</em></h2>
  <div class="dots"></div>
  <div class="process-steps">
    <div class="process-line" style="left:192px"></div>
    <div class="process-line" style="left:378px"></div>
    <div class="process-line" style="left:565px"></div>
    <div class="process-line" style="left:752px"></div>
    <div class="process-line" style="left:936px"></div>

    <div class="step" style="left:132px"><div class="step-icon">
      <svg width="50" height="50" viewBox="0 0 50 50" fill="none" stroke="#fff" stroke-width="2"><path d="M8 16l18-8 18 8-18 8z"/><path d="M8 16v18l18 8 18-8V16"/><path d="M26 24v18"/><circle cx="14" cy="36" r="6" fill="#e8362f"/><path d="M11 36l2 2 4-4"/></svg>
    </div><div class="step-label">Receive / Sender</div></div>

    <div class="step" style="left:318px"><div class="step-icon">
      <svg width="50" height="50" viewBox="0 0 50 50" fill="none" stroke="#fff" stroke-width="2"><rect x="13" y="9" width="24" height="33"/><path d="M18 6h14v5H18zM18 20h14M18 26h14M18 32h14"/></svg>
    </div><div class="step-label">Transera</div></div>

    <div class="step" style="left:505px"><div class="step-icon">
      <svg width="50" height="50" viewBox="0 0 50 50" fill="none" stroke="#fff" stroke-width="2"><rect x="10" y="12" width="16" height="16"/><path d="M15 22v-6l-2 2M21 22v-6l2 2M30 20h10l-3-3M40 20l-3 3"/><rect x="7" y="32" width="36" height="9" rx="4.5"/><circle cx="13" cy="36.5" r="1.5"/><circle cx="21" cy="36.5" r="1.5"/><circle cx="29" cy="36.5" r="1.5"/><circle cx="37" cy="36.5" r="1.5"/></svg>
    </div><div class="step-label">Supplier</div></div>

    <div class="step" style="left:692px"><div class="step-icon">
      <svg width="50" height="50" viewBox="0 0 50 50" fill="none" stroke="#fff" stroke-width="2"><rect x="6" y="12" width="24" height="20"/><path d="M30 18h8l6 7v7H30z"/><circle cx="14" cy="35" r="3.5"/><circle cx="37" cy="35" r="3.5"/><path d="M12 22h12l-3-3M24 22l-3 3"/></svg>
    </div><div class="step-label">Carrier</div></div>

    <div class="step" style="left:876px"><div class="step-icon active">
      <svg width="50" height="50" viewBox="0 0 50 50" fill="none" stroke="#fff" stroke-width="2"><rect x="14" y="6" width="22" height="36"/><rect x="19" y="22" width="6" height="6"/><rect x="25" y="28" width="6" height="6"/><rect x="19" y="28" width="6" height="6"/><circle cx="18" cy="44" r="2"/><circle cx="32" cy="44" r="2"/></svg>
    </div><div class="step-label active">Transera</div></div>

    <div class="step" style="left:1060px"><div class="step-icon">
      <svg width="50" height="50" viewBox="0 0 50 50" fill="none" stroke="#fff" stroke-width="2"><rect x="6" y="14" width="24" height="18"/><path d="M30 20h8l6 6v6H30z"/><circle cx="14" cy="35" r="3.5"/><circle cx="37" cy="35" r="3.5"/></svg>
    </div><div class="step-label">Shipped</div></div>
  </div>
</section>

<section class="testimonials">
  <h2 class="section-title">What <em>People Say</em></h2>
  <div class="dots"></div>
  <div class="divider-v"></div>
  <div class="divider-h"></div>

  <div class="quote left" style="left:51px;top:102px">
    <div><p>Duis aute irure dolor in reprehenderit in voluptate velit esse cillum dolore eu fugiat nulla pariatur. Excepteur sint occaecat cupidatat non proident, sunt in culpa qui officia deserunt mollit.</p><cite>Evan Marlow, Operations Manager</cite></div>
    <div class="avatar" role="img" aria-label="Portrait of Evan Marlow"></div>
  </div>
  <div class="quote" style="left:634px;top:102px">
    <div class="avatar" role="img" aria-label="Portrait of Rosa Tennant"></div>
    <div><p>Provident, similique sunt in culpa qui officia deserunt mollitia animi, id est laborum et dolorum fuga. Et harum quidem rerum facilis est et expedita distinctio. Nam libero tempore, cum soluta nobis.</p><cite>Rosa Tennant, Creative Designer</cite></div>
  </div>
  <div class="quote left" style="left:51px;top:239px">
    <div><p>Luis aute irure dolor in reprehenderit in piluptate velit esse cillum dolore eu fugiat nulla pariatur. Excepteur sint occaecat cupidatat non proident, sunt in culpa qui officia deserunt mollit.</p><cite>Nadia Pruett, Manager</cite></div>
    <div class="avatar" role="img" aria-label="Portrait of Nadia Pruett"></div>
  </div>
  <div class="quote" style="left:634px;top:239px">
    <div class="avatar" role="img" aria-label="Portrait of Owen Fairley"></div>
    <div><p>At vero eos et accusamus et iusto odio dignissimos ducimus qui blanditiis praesentium voluptatum deleniti atque corrupti quos dolores et quas molestias excepturi sint occaecati asperiores.</p><cite>Owen Fairley, Developer</cite></div>
  </div>
</section>

<section class="mail-strip">
  <svg width="36" height="32" viewBox="0 0 36 32" fill="none" stroke="#e8362f" stroke-width="2" stroke-linejoin="round"><path d="M34 2L2 14l12 4 4 12 4-9z"/><path d="M34 2L14 18"/></svg>
  <span class="lbl">Feel Free to Mail</span>
  <div class="field">Full Name *</div>
  <div class="field">Phone Number *</div>
  <div class="field">Your Email *</div>
  <div class="submit">SUBMIT</div>
</section>

<footer class="site-footer">
  <div class="footer-col contact-col">
    <h3>Contact Us</h3>
    <p>Please feel free to contact us for any issue. Our staff is available to you from 9AM until 5PM on weekdays.</p>
    <p><strong>Phone:</strong> +1-800-555-0187</p>
    <p><strong>Office:</strong> Harborview Depot</p>
    <p><strong>Email:</strong> dispatch@tandemrailhaul.example</p>
    <div class="foot-social"><span></span><span></span><span></span><span></span><span></span></div>
  </div>
  <div class="footer-col hq-col">
    <h3>Headquarters</h3>
    <div class="map" role="img" aria-label="Street map showing the headquarters location by the harbor"></div>
  </div>
  <div class="footer-col about-col">
    <h3>About Team</h3>
    <p>Enim congue blandit. Lorem ipsum dolor sit amet, consectetur adipiscing elit. Quisque consectetur interdum finibus. Vestibulum ante ipsum primis in faucibus orci. luctus et ultrices posuere.</p>
    <p>Cubilia cras blandit finibus ipsum, id porttitor arcu volutpat a. Integer iaculis erat nec justo malesuada faucibus vel tempus sapien. Vivamus aliquam euismod tristique.</p>
  </div>
  <div class="footer-rule"></div>
  <div class="footer-bottom">
    <span>Copyright © 2017 Tandem Rail Haul INC</span>
    <span class="footer-brand"><span class="brand-dot"></span>Tandem Rail Haul INC</span>
    <span>All rights reserved</span>
  </div>
  <div class="bottom-strip"></div>
</footer>
</body>
</html>
```